Brochure Design Project - Brelwick Motors Auto Repair Centre

We require a high quality brochure (A3 folded to A4) for us to send to local businesses to try and get more sales. We would like to keep our current colour scheme from our flyers. We are garagemark approved so we require this logo to be included in the design. The font used on our flyer is QuickLinesRG available from fontvault-example.com
This is a brief of the information we require on our brochure (the feedback from our current customers still to be received but it will be limited to 1 line each) :
Introduction to Brelwick Motors
Based in Cumbernauld, Brelwick Motors are a family run Auto service centre and believe in giving helpful, friendly expert advice in plain English. We have a wealth of experience in a wide range of vehicles and we invest heavily in equipment to ensure our work is completed to the highest possible quality standards.
It is our aim to deliver a quality service at competitive rates for our customers. We have just expanded by investing in a new 4000 sq/ft workshop to help support our ever expanding customer base.
Why are we the best choice for your business?
Choosing a garage for your business can be a tough decision. Who do you choose and who do you trust? Cost will of course be high on your list, so why take your car to a main dealer and pay main dealer prices?
• Brelwick Motors Cumbernauld can carry out servicing and repairs to main dealer standards without the high prices. We can also maintain your vehicles warranty by using genuine manufacturer's parts.
• Communication is key – we never leave you wondering when your vehicle is going to be returned. 98% of vehicles we maintain are returned the same day.
• We never carry out any work to a vehicle without prior agreement – so no unexpected bills. You always get a fully itemised VAT invoice.
• We can arrange payment terms that are suitable to both businesses.
• We have flexibility with our working hours to ensure your fleet stays on the road no matter how big or small.
• We also pride ourselves on providing a professional and efficient service, your vehicle will be looked after as if it was our own pride and joy.
How can we guarantee quality?
Garage mark is the Trading Standards code of practice for garages. We are the only independent garage in Cumbernauld to achieve this standard. We are audited to ensure we comply with the code at all times and we must follow a strict complaints procedure should the need arise.
All parts fitted are covered by a 3 month or 6000 mile warranty. *Does not include wear and tear
What services can we offer your business?
MOT Testing
Vehicle Servicing
Budget & Performance Tyres
Mechanical Repairs
Exhausts, DPF filters & CAT’s
Brake repair specialist
Same day Clutch repairs
Gearboxes
Starter motors
Alternators
Wheel Alignment
MOT Welding
Replacement Batteries
ECU Fault Diagnostics & Service resets
Collection and drop off services
We are comprehensively insured to drive all of our customers’ vehicles so we can collect vehicles at a time that suits you and deliver them back with minimal impact to your business. The only time we will ever drive your vehicles is during transportation or testing.
Our current business customers – testimonials
Pettigrew Roofing
Crest Fitting
Hollowbys
Ruvan Loader training
Sample price list
£74.17 for car service/small vans
£91.67 for commercials up to 3500kgs (class IV)
Mot’s £35 for cars and vans (class IV)
Tyre sample prices – Ford Focus £36.95, Renault Kangoo £32.45, Ford Transit £41.55.
Labour rate of £35.00ph
All prices exclude VAT at applicable rate, unless stated otherwise and are correct at time of printing. Subject to change without prior notice. No VAT on MOT's
Contact Us
Brelwick Motors can be contacted to discuss your individual requirement by -
Phone: 01236 482915
Email: sales@brelwick-example.co.uk
Mon – Fri 8.00am – 5.30pm
Sat – 8.00am – 4.00pm
Target Market(s)
local businesses
Industry/Entity Type
Garage
Requirements
Must have
- garagemark logo
brelwick motors logo

```html
<!DOCTYPE html>
<html lang="en">
<head>
<meta charset="utf-8">
<title>Brelwick Motors Auto Repair Centre – Brochure Cover</title>
<link rel="stylesheet" href="https://fonts.googleapis.com/css2?family=Exo+2:wght@600;700&display=swap">
<style>
  :root {
    --page-bg: #ececec;
    --steel-deep: #0f2a47;
    --steel-mid: #3f78b4;
    --steel-light: #9cc6ea;
    --sky-light: #eef5fb;
    --wall-blue: #8db3d9;
    --signal-yellow: #e9e21a;
    --olive-yellow: #9a9514;
    --panel-navy: #1c3555;
    --text-white: #ffffff;
  }
  * { margin: 0; padding: 0; box-sizing: border-box; }
  html, body {
    width: 1200px;
    height: 848px;
    overflow: hidden;
    background: var(--page-bg);
    font-family: "Exo 2", sans-serif;
  }
  .brochure-cover {
    position: absolute;
    left: 320px;
    top: 29px;
    width: 560px;
    height: 790px;
    overflow: hidden;
    background: var(--steel-deep);
  }
  .cover-art {
    position: absolute;
    inset: 0;
    width: 560px;
    height: 790px;
  }
  .brand-name {
    position: absolute;
    left: 150px;
    top: 178px;
    width: 380px;
    text-align: right;
    color: var(--text-white);
    font-weight: 700;
    font-size: 50px;
    line-height: 1;
    letter-spacing: 1px;
    text-transform: uppercase;
  }
  .brand-name span { display: block; }
  .service-list {
    position: absolute;
    left: 45px;
    top: 600px;
    width: 475px;
    list-style: none;
    color: var(--text-white);
    font-weight: 600;
    font-size: 12.5px;
    line-height: 1;
    text-align: center;
  }
  .service-row {
    display: flex;
    justify-content: center;
    align-items: center;
    gap: 9px;
    margin-bottom: 9px;
  }
  .service-row.spaced { margin-top: 6px; }
  .divider {
    width: 10px;
    height: 10px;
    background: var(--signal-yellow);
    flex: none;
  }
</style>
</head>
<body>
  <main class="brochure-cover">
    <svg class="cover-art" viewBox="0 0 560 790" aria-hidden="false">
      <defs>
        <linearGradient id="glassGradient" x1="0" y1="0" x2="1" y2="1">
          <stop offset="0" stop-color="#1d4470"/>
          <stop offset="0.45" stop-color="#4f8ac4"/>
          <stop offset="1" stop-color="#173a60"/>
        </linearGradient>
        <linearGradient id="buildingGradient" x1="0" y1="0" x2="0" y2="1">
          <stop offset="0" stop-color="#f4f8fc"/>
          <stop offset="0.4" stop-color="#a9c7e4"/>
          <stop offset="1" stop-color="#5f8fc0"/>
        </linearGradient>
        <linearGradient id="yellowGradient" x1="0" y1="0" x2="1" y2="1">
          <stop offset="0" stop-color="#f0ea2a"/>
          <stop offset="0.5" stop-color="#c9c214"/>
          <stop offset="1" stop-color="#8e8a10"/>
        </linearGradient>
      </defs>

      <rect class="glass-backdrop" x="0" y="0" width="560" height="790" fill="url(#glassGradient)"
            role="img" aria-label="Abstract photograph of blue glass and steel architecture"/>

      <polygon class="garage-photo" points="0,400 514,334 330,560 0,640"
               fill="url(#buildingGradient)"
               role="img" aria-label="Photograph of the garage building with reception sign"/>

      <polyline points="0,400 514,334 330,560" fill="none" stroke="var(--signal-yellow)" stroke-width="6"/>

      <polygon class="yellow-sweep" points="0,640 330,560 430,520 560,505 560,790 0,790"
               fill="url(#yellowGradient)"/>
      <polygon points="0,700 560,610 560,790 0,790" fill="var(--olive-yellow)" opacity="0.35"/>

      <polygon class="services-panel" points="35,593 525,556 507,715 49,742"
               fill="var(--panel-navy)" stroke="var(--signal-yellow)" stroke-width="3"/>
    </svg>

    <h1 class="brand-name"><span>Brelwick</span><span>Motors</span></h1>

    <ul class="service-list">
      <li class="service-row">MOT Testing <i class="divider"></i> Vehicle Servicing <i class="divider"></i> Budget &amp; Performance Tyres</li>
      <li class="service-row">Mechanical Repairs <i class="divider"></i> Exhausts, DPF filters &amp; CAT’s</li>
      <li class="service-row">Brake repair specialist <i class="divider"></i> Same day Clutch repairs <i class="divider"></i> Gearboxes</li>
      <li class="service-row spaced">Starter motors <i class="divider"></i> Alternators <i class="divider"></i> Wheel Alignment <i class="divider"></i> MOT Welding</li>
      <li class="service-row">Replacement Batteries <i class="divider"></i> ECU Fault Diagnostics &amp; Service resets</li>
    </ul>
  </main>
</body>
</html>
```